Modern corporate energy/fuel business need business card design

Business card required for company founder. Korvan Adaptive Energy is a Australian based modern energy/fuel provider. We offer specialised solutions to businesses using fossil fuels through renewable energy solutions.

I would like one side with specific information (name, address etc)

The other side to be bold, professional company name & logo. Striking.

Target Market(s)

B2B. Transport, mining, councils, environmentalist,

Industry/Entity Type

Petroleum

Contact Information for Business Card

Name; Peter Morrow
Position; Director
Email; pmorrow@korvanae.com.au
Address; PO Box 347, Lindale, QLD, 4170
Website; www.korvanae.com.au

Colors

Designer to choose colors to be used in the design.

Requirements
Must have
• Clean, easy to read, professional & strong theme
Should not have
• too many colours, busy layout,

```html
<!DOCTYPE html>
<html lang="en">
<head>
<meta charset="utf-8">
<title>Korvan Adaptive Energy – Business Card</title>
<link rel="stylesheet" href="https://fonts.googleapis.com/css2?family=Arimo:wght@400;700&display=swap">
<style>
  :root {
    --backdrop: #f7e3ef;
    --navy: #2b5575;
    --navy-deep: #24506f;
    --orange: #f0701a;
    --cream: #eef0e2;
    --steel: #8fa6b8;
    --ink: #1a1a1a;
    --white: #ffffff;
  }
  * { margin: 0; padding: 0; box-sizing: border-box; }
  html, body {
    width: 1200px; height: 800px; overflow: hidden;
    background: var(--backdrop);
    font-family: "Arimo", Arial, sans-serif;
  }
  .canvas { position: relative; width: 1200px; height: 800px; }
  .card {
    position: absolute;
    width: 560px; height: 320px;
    border-radius: 26px;
    overflow: hidden;
    box-shadow: 0 8px 22px rgba(60, 30, 50, 0.18);
  }

  /* Front side */
  .card-front { left: 60px; top: 90px; background: var(--white); }
  .card-front .swoosh { position: absolute; inset: 0; width: 560px; height: 320px; }
  .brand {
    position: absolute; left: 34px; top: 32px;
    display: flex; align-items: center; gap: 14px;
  }
  .brand-dot {
    width: 46px; height: 46px; border-radius: 50%;
    background: var(--orange); flex: none;
  }
  .brand-name {
    color: var(--navy); font-weight: 700; font-size: 22px;
    letter-spacing: 1px; text-transform: uppercase; line-height: 1.1;
  }
  .address {
    position: absolute; left: 40px; top: 128px;
    font-size: 15px; color: var(--ink);
  }
  .contact {
    position: absolute; left: 40px; top: 162px;
    list-style: none; font-size: 15px; color: var(--ink);
  }
  .contact li { display: flex; align-items: center; gap: 8px; margin-bottom: 5px; }
  .contact svg { width: 16px; height: 16px; flex: none; }
  .person {
    position: absolute; right: 40px; top: 172px; text-align: right;
  }
  .person-name { color: var(--navy); font-weight: 700; font-size: 22px; }
  .person-role { color: var(--ink); font-size: 21px; margin-top: 2px; }

  /* Back side */
  .card-back {
    left: 580px; top: 420px;
    background: linear-gradient(150deg, var(--navy-deep) 0%, #7f9bab 28%, var(--cream) 48%, #c5cfcf 62%, var(--navy-deep) 100%);
  }
  .back-brand {
    position: absolute; left: 0; right: 0; top: 118px;
    display: flex; justify-content: center; align-items: center; gap: 16px;
  }
  .back-brand .brand-dot { width: 58px; height: 58px; }
  .back-brand .brand-name { font-size: 28px; }
  .back-web {
    position: absolute; left: 0; right: 0; bottom: 50px; text-align: center;
    font-size: 15px; color: var(--ink);
  }
  .back-web .accent { color: var(--orange); }
</style>
</head>
<body>
<main class="canvas">

  <section class="card card-front" aria-label="Business card front">
    <svg class="swoosh" viewBox="0 0 560 320" aria-hidden="true">
      <path d="M0,258 Q270,312 560,272 L560,320 L0,320 Z" fill="var(--navy)"/>
      <path d="M0,232 Q220,268 480,308 Q240,272 0,252 Z" fill="var(--orange)"/>
      <path d="M130,250 Q310,280 490,308 Q300,286 160,256 Z" fill="var(--steel)" opacity="0.8"/>
    </svg>
    <div class="brand">
      <span class="brand-dot"></span>
      <span class="brand-name">Korvan<br>Adaptive Energy</span>
    </div>
    <p class="address">PO Box 347, Lindale, QLD, 4170</p>
    <ul class="contact">
      <li>
        <svg viewBox="0 0 16 16"><rect x="1" y="3" width="14" height="10" fill="var(--navy)"/><path d="M1,3 L8,9 L15,3" fill="none" stroke="#fff" stroke-width="1.2"/></svg>
        pmorrow@korvanae.com.au
      </li>
      <li>
        <svg viewBox="0 0 16 16" fill="none" stroke="var(--navy)" stroke-width="1.1"><circle cx="8" cy="8" r="6.5"/><ellipse cx="8" cy="8" rx="3" ry="6.5"/><path d="M1.5,8 H14.5 M2.5,4.5 H13.5 M2.5,11.5 H13.5"/></svg>
        www.korvanae.com.au
      </li>
    </ul>
    <div class="person">
      <p class="person-name">Peter Morrow</p>
      <p class="person-role">Director</p>
    </div>
  </section>

  <section class="card card-back" aria-label="Business card back">
    <div class="back-brand">
      <span class="brand-dot"></span>
      <span class="brand-name">Korvan<br>Adaptive Energy</span>
    </div>
    <p class="back-web">www.<span class="accent">korvanae</span>.com.au</p>
  </section>

</main>
</body>
</html>
```